Lend a Lantern Website Design (design layout only)

We need a website design for a new nonprofit organization based in Des Moines, Iowa called Lend a Lantern. The nonprofit provides soccer training opportunities to youth soccer players looking to improve their game while also affecting the lives of the less fortunate in a positive way. While participating in the training programs the players also go out and raise money for selected charities. The organization then donates the funds. In its first 18 months we donated $10,500. We would like to see designs attempt to symbolize the mission of the nonprofit - essentially "improve you while improving someone else."

We would like to see the following features:

· A place to donate - Our intent is to have the home page linked to the donation page; a simple straight-forward process for people to give money, and make donating as painless as possible - no account needed to make a donation, credit card or e-check should be the only information needed to donate, and have it be on a single page.

· A photo gallery so people can browse the photo gallery to get a better understanding of our organization and a place to add videos and a calendar to show upcoming events

· A place for contact information and the profiles of directors and board members. This should include a spot showing all the charities the organization donates to. Also includes a news section/blog for comments and suggestions.

We want the design to revolve around the content and mission. We would really like to stress our organization as nonprofit. We would also like if the website was user friendly and easy to navigate.

The logo of our organization is uploaded

```html
<!DOCTYPE html>
<html lang="en">
<head>
<meta charset="utf-8">
<title>Lend a Lantern</title>
<link href="https://fonts.googleapis.com/css2?family=Arvo:wght@400;700&family=Open+Sans:wght@400;600;700&display=swap" rel="stylesheet">
<style>
:root{
  --green:#6e9a48;
  --green-dark:#4a6b2d;
  --green-text:#5c8a37;
  --gray-text:#7a7a7a;
  --gray-head:#8a8a8a;
  --gray-line:#cfcfcf;
  --band:#f3f3f3;
  --white:#ffffff;
}
*{margin:0;padding:0;box-sizing:border-box}
html,body{width:1200px;height:2361px;overflow:hidden;background:var(--white)}
body{position:relative;font-family:"Open Sans",Arial,sans-serif;color:var(--gray-text)}
.abs{position:absolute}

/* top bar */
.topbar{left:0;top:0;width:1200px;height:40px;background:var(--green)}
.top-social{top:7px;width:26px;height:26px;border:1px solid rgba(255,255,255,.5);border-radius:3px}
.top-social::after{content:"";position:absolute;left:9px;top:9px;width:6px;height:6px;border-radius:50%;background:#fff}
.top-phone{left:531px;top:0;height:40px;color:#fff;font-size:16px;display:flex;align-items:center;gap:8px}
.top-link{top:0;line-height:40px;color:#fff;font-size:14px;font-family:"Arvo",Georgia,serif}
.top-sep{top:12px;width:1px;height:16px;background:rgba(255,255,255,.5)}
.top-donate{left:889px;top:0;width:138px;height:40px;background:var(--green-dark);color:#fff;font-size:13px;line-height:40px;text-align:center;font-family:"Arvo",Georgia,serif}

/* header */
.brand{left:173px;top:72px;display:flex;align-items:center;gap:14px}
.brand .mark{width:60px;height:60px;background:var(--green);border-radius:50%}
.brand .name{font-family:"Arvo",Georgia,serif;font-weight:700;font-size:34px;color:var(--green-text);line-height:1}
.nav{top:100px;font-family:"Arvo",Georgia,serif;font-size:14px;color:var(--gray-head)}
.nav.active{color:var(--green-text)}

/* hero */
.hero{left:0;top:171px;width:1200px;height:553px;background:linear-gradient(100deg,#d9d2c6 0%,#9b8a78 25%,#5a6d8a 45%,#8a6a55 60%,#2c2c2c 80%,#b9a592 100%)}
.hero-arrow{top:357px;width:34px;height:96px;border:2px solid rgba(255,255,255,.6);background:rgba(0,0,0,.1)}
.headline{background:rgba(94,140,56,.85);color:#fff;font-family:"Arvo",Georgia,serif;font-weight:700;text-align:center;white-space:nowrap}
.hero-donate{left:509px;top:494px;width:183px;height:59px;border:2px solid #fff;background:rgba(0,0,0,.35);color:#fff;font-family:"Arvo",Georgia,serif;font-size:19px;line-height:55px;text-align:center}
.dot{top:696px;width:11px;height:11px;border-radius:50%;background:#fff}

/* raised */
.raised-title{left:0;width:1200px;top:740px;text-align:center;font-family:"Arvo",Georgia,serif;font-size:52px;color:var(--gray-head)}
.digits{left:325px;top:818px;display:flex;gap:8px}
.digit{width:87px;height:87px;border-radius:50%;border:3px solid #e2e2e2;font-family:"Arvo",Georgia,serif;font-size:46px;color:var(--green-dark);text-align:center;line-height:80px}
.digit.currency{border-color:var(--green)}
.raised-copy{left:260px;width:680px;top:922px;text-align:center;font-size:16px;line-height:24px}
.btn-outline{border:2px solid var(--green);color:var(--green-text);font-family:"Arvo",Georgia,serif;font-size:19px;text-align:center}

/* gallery */
.gallery{left:0;top:1078px;width:1200px;height:319px;background:var(--band)}
.section-title{font-family:"Arvo",Georgia,serif;font-size:32px;color:var(--gray-head)}
.gallery-photo{top:1153px;width:205px;height:205px;border-radius:50%;border:4px solid #9a9a9a}

/* video & events */
.video{left:173px;top:1469px;width:439px;height:234px;background:linear-gradient(135deg,#3a6f8a,#6b4e3d 55%,#2e4f2a);border-radius:3px}
.play{left:349px;top:1520px;width:88px;height:88px;border-radius:50%;border:4px solid rgba(255,255,255,.8);background:rgba(0,0,0,.35)}
.video-caption{left:173px;width:439px;top:1620px;text-align:center;color:#fff;font-family:"Arvo",Georgia,serif;font-size:30px}
.event-photo{left:686px;width:132px;height:113px;border:2px solid #ddd}
.event-date{left:883px;font-family:"Arvo",Georgia,serif;font-size:19px;color:var(--green-dark)}
.event-title{left:838px;font-family:"Arvo",Georgia,serif;font-size:18px;color:var(--green-text)}
.event-copy{left:838px;width:160px;font-size:11px;line-height:15px}

/* profiles */
.profile-photo{top:1798px;width:126px;height:126px;border-radius:50%;border:3px solid #ccc}
.profile-role{font-family:"Arvo",Georgia,serif;color:var(--green-text);text-align:center}
.btn-profile{top:1961px;width:106px;height:34px;border:2px solid #ccc;font-family:"Arvo",Georgia,serif;font-size:12px;line-height:30px;text-align:center;color:var(--gray-head)}
.map{left:671px;top:1794px;width:358px;height:181px;background:linear-gradient(135deg,#e9e6dd,#d8dccb 50%,#ece9e0);border:2px solid #ccc}
.map-name{left:722px;top:1866px;display:flex;align-items:center;gap:10px;font-family:"Arvo",Georgia,serif;font-weight:700;font-size:24px;color:var(--green-text)}
.map-name .sq{width:32px;height:32px;background:var(--green)}
.contact-icon{top:1996px;width:38px;height:38px;border-radius:50%;border:2px solid var(--green-text)}
.contact-text{top:2005px;font-size:11px}

/* footer */
.footer{left:0;top:2059px;width:1200px;height:258px;background:var(--green)}
.foot-title{top:2084px;font-family:"Arvo",Georgia,serif;font-size:27px;color:#fff}
.foot-rule{top:2128px;width:200px;height:1px;background:rgba(255,255,255,.45)}
.foot-copy{color:#fff;font-size:11px;line-height:15px}
.foot-copy b{font-weight:700}
.foot-thumb{width:60px;height:50px;border:2px solid #fff;background:linear-gradient(135deg,#a8a29a,#6b6b6b)}
.foot-social{color:#fff;font-size:12px;font-weight:600;display:flex;align-items:center;gap:12px}
.foot-social i{width:14px;height:14px;border-radius:50%;background:#fff;display:inline-block;opacity:.85}
.foot-news{width:60px;height:52px;border:2px solid #fff;background:linear-gradient(#9fb9d8,#6f9a48)}
.copyright{left:0;width:1200px;top:2328px;text-align:center;font-size:12px;color:#666}
</style>
</head>
<body>

<!-- top bar -->
<div class="abs topbar"></div>
<div class="abs top-social" style="left:173px"></div>
<div class="abs top-social" style="left:205px"></div>
<div class="abs top-social" style="left:237px"></div>
<div class="abs top-phone">
  <svg width="18" height="18" viewBox="0 0 24 24" fill="#fff"><path d="M6.6 10.8a15.1 15.1 0 0 0 6.6 6.6l2.2-2.2c.3-.3.7-.4 1-.2 1.1.4 2.3.6 3.6.6.6 0 1 .4 1 1V20c0 .6-.4 1-1 1C10.6 21 3 13.4 3 4c0-.6.4-1 1-1h3.5c.6 0 1 .4 1 1 0 1.3.2 2.5.6 3.6.1.3 0 .7-.2 1z"/></svg>
  0800-555-0199
</div>
<div class="abs top-link" style="left:716px">Sign Up</div>
<div class="abs top-sep" style="left:784px"></div>
<div class="abs top-link" style="left:808px">Login</div>
<div class="abs top-sep" style="left:866px"></div>
<div class="abs top-donate">DONATE NOW</div>

<!-- header -->
<div class="abs brand"><span class="mark"></span><span class="name">LEND A<br>LANTERN</span></div>
<div class="abs nav active" style="left:608px">HOME</div>
<div class="abs nav" style="left:686px">ABOUT</div>
<div class="abs nav" style="left:770px">DONATION</div>
<div class="abs nav" style="left:881px">BLOG</div>
<div class="abs nav" style="left:956px">CONTACT</div>

<!-- hero -->
<div class="abs hero" role="img" aria-label="Photo of a youth soccer team lined up with coaches on a field"></div>
<div class="abs hero-arrow" style="left:0"></div>
<div class="abs hero-arrow" style="left:1166px"></div>
<div class="abs headline" style="left:360px;top:350px;width:486px;height:53px;font-size:44px;line-height:53px">improve you while</div>
<div class="abs headline" style="left:275px;top:405px;width:640px;height:59px;font-size:44px;line-height:57px">improving someone else !</div>
<div class="abs hero-donate">DONATE</div>
<div class="abs dot" style="left:590px"></div>
<div class="abs dot" style="left:609px"></div>

<!-- raised -->
<div class="abs raised-title">YOU'VE HELPED RAISE</div>
<div class="abs digits">
  <div class="digit currency">$</div><div class="digit">1</div><div class="digit">0</div><div class="digit">5</div><div class="digit">0</div><div class="digit">0</div>
</div>
<p class="abs raised-copy">Lorem ipsum dolor sit amet, consectetuer adipiscing elit, sed diam nonummynibh nibh euismod tincidunt ut laoreet dolore magna aliquam erat volutpat. liqua volutpat.</p>
<div class="abs btn-outline" style="left:509px;top:999px;width:179px;height:59px;line-height:55px">DONATE</div>

<!-- gallery -->
<div class="abs gallery"></div>
<div class="abs section-title" style="left:0;width:1200px;text-align:center;top:1104px">GALLERY</div>
<div class="abs gallery-photo" style="left:173px;background:linear-gradient(#c9d6c0,#4f8a36)" role="img" aria-label="Young players contesting the ball"></div>
<div class="abs gallery-photo" style="left:389px;background:linear-gradient(#cfe0ef,#5a9a3c)" role="img" aria-label="Kids running after the ball in a match"></div>
<div class="abs gallery-photo" style="left:606px;background:linear-gradient(#a7b59a,#4d7a30)" role="img" aria-label="Soccer ball resting on grass near a goal"></div>
<div class="abs gallery-photo" style="left:822px;background:linear-gradient(#8fb4dc,#8d8a7a 45%,#5f8e3a)" role="img" aria-label="Field with mountains in the background"></div>

<!-- video & events -->
<div class="abs section-title" style="left:173px;top:1410px">VIDEO</div>
<div class="abs video" role="img" aria-label="Team hands stacked on a soccer ball"></div>
<div class="abs play"></div>
<svg class="abs" style="left:381px;top:1546px" width="32" height="36" viewBox="0 0 32 36"><polygon points="0,0 32,18 0,36" fill="rgba(255,255,255,.85)"/></svg>
<div class="abs video-caption">Watch A Video</div>

<div class="abs section-title" style="left:686px;top:1410px">EVENTS</div>
<div class="abs event-photo" style="top:1467px;background:linear-gradient(#cfe0ef,#5a9a3c)" role="img" aria-label="Youth match in progress"></div>
<svg class="abs" style="left:838px;top:1473px" width="34" height="32" viewBox="0 0 34 32"><rect x="1" y="4" width="32" height="27" fill="none" stroke="#4a6b2d" stroke-width="2"/><rect x="1" y="4" width="32" height="7" fill="#4a6b2d"/><rect x="8" y="0" width="3" height="7" fill="#4a6b2d"/><rect x="23" y="0" width="3" height="7" fill="#4a6b2d"/><g fill="#4a6b2d"><rect x="6" y="15" width="5" height="4"/><rect x="14" y="15" width="5" height="4"/><rect x="22" y="15" width="5" height="4"/><rect x="6" y="22" width="5" height="4"/><rect x="14" y="22" width="5" height="4"/></g></svg>
<div class="abs event-date" style="top:1474px">29 JULY 2014</div>
<div class="abs event-title" style="top:1505px">Lorem ipsum dolor</div>
<p class="abs event-copy" style="top:1532px">Lorem ipsum dolor sit amet, consectetuer adipiscing elit, sed .adipiscing elit</p>
<div class="abs event-photo" style="top:1591px;background:linear-gradient(#8fb4dc,#8d8a7a 45%,#5f8e3a)" role="img" aria-label="Players on a field below mountains"></div>
<svg class="abs" style="left:838px;top:1596px" width="34" height="32" viewBox="0 0 34 32"><rect x="1" y="4" width="32" height="27" fill="none" stroke="#4a6b2d" stroke-width="2"/><rect x="1" y="4" width="32" height="7" fill="#4a6b2d"/><rect x="8" y="0" width="3" height="7" fill="#4a6b2d"/><rect x="23" y="0" width="3" height="7" fill="#4a6b2d"/><g fill="#4a6b2d"><rect x="6" y="15" width="5" height="4"/><rect x="14" y="15" width="5" height="4"/><rect x="22" y="15" width="5" height="4"/><rect x="6" y="22" width="5" height="4"/><rect x="14" y="22" width="5" height="4"/></g></svg>
<div class="abs event-date" style="top:1597px">29 JULY 2014</div>
<div class="abs event-title" style="top:1628px">Lorem ipsum dolor</div>
<p class="abs event-copy" style="top:1655px">Lorem ipsum dolor sit amet, consectetuer adipiscing elit, sed .adipiscing elit</p>

<!-- profiles -->
<div class="abs section-title" style="left:173px;top:1732px">PROFILES</div>
<div class="abs profile-photo" style="left:175px;background:linear-gradient(#f0f0f0,#6a6a72)" role="img" aria-label="Portrait of the director"></div>
<div class="abs profile-role" style="left:175px;width:126px;top:1929px;font-size:18px">Director</div>
<div class="abs btn-profile" style="left:187px">PROFILE</div>
<div class="abs profile-photo" style="left:391px;background:linear-gradient(#f5f5f5,#7a5b50)" role="img" aria-label="Portrait of a board member"></div>
<div class="abs profile-role" style="left:381px;width:146px;top:1922px;font-size:27px">Member</div>
<div class="abs btn-profile" style="left:401px">PROFILE</div>

<!-- contact -->
<div class="abs section-title" style="left:686px;top:1732px">CONTACT US</div>
<div class="abs map" role="img" aria-label="Street map showing the office location"></div>
<div class="abs map-name"><span class="sq"></span>LEND A LANTERN</div>
<div class="abs contact-icon" style="left:673px"></div>
<svg class="abs" style="left:683px;top:2006px" width="18" height="18" viewBox="0 0 24 24" fill="#5c8a37"><path d="M6.6 10.8a15.1 15.1 0 0 0 6.6 6.6l2.2-2.2c.3-.3.7-.4 1-.2 1.1.4 2.3.6 3.6.6.6 0 1 .4 1 1V20c0 .6-.4 1-1 1C10.6 21 3 13.4 3 4c0-.6.4-1 1-1h3.5c.6 0 1 .4 1 1 0 1.3.2 2.5.6 3.6.1.3 0 .7-.2 1z"/></svg>
<div class="abs contact-text" style="left:722px">0800-555-0199</div>
<div class="abs contact-icon" style="left:841px"></div>
<svg class="abs" style="left:852px;top:2005px" width="16" height="20" viewBox="0 0 16 20"><path d="M8 0a8 8 0 0 0-8 8c0 6 8 12 8 12s8-6 8-12a8 8 0 0 0-8-8zm0 11a3 3 0 1 1 0-6 3 3 0 0 1 0 6z" fill="#5c8a37"/></svg>
<div class="abs contact-text" style="left:891px">123-Lorem ipsum dolor .</div>

<!-- footer -->
<div class="abs footer"></div>
<div class="abs foot-title" style="left:173px">CHIRPS</div>
<div class="abs foot-rule" style="left:173px"></div>
<p class="abs foot-copy" style="left:173px;top:2148px;width:200px"><b>Lorem ipsum dolor</b><br>sit amet, consectetuer adipiscing elit, sed .</p>
<div class="abs foot-copy" style="left:298px;top:2191px">@chirps</div>
<p class="abs foot-copy" style="left:173px;top:2215px;width:200px"><b>Lorem ipsum dolor</b><br>sit amet, consectetuer adipiscing elit, sed .</p>
<div class="abs foot-copy" style="left:298px;top:2255px">@chirps</div>

<div class="abs foot-title" style="left:389px">BLOG</div>
<div class="abs foot-rule" style="left:389px;width:190px"></div>
<div class="abs foot-thumb" style="left:409px;top:2146px" role="img" aria-label="Author portrait"></div>
<div class="abs foot-thumb" style="left:483px;top:2146px" role="img" aria-label="Author portrait"></div>
<div class="abs foot-thumb" style="left:409px;top:2214px" role="img" aria-label="Author portrait"></div>
<div class="abs foot-thumb" style="left:483px;top:2214px" role="img" aria-label="Author portrait"></div>

<div class="abs foot-title" style="left:608px">SOCIAL</div>
<div class="abs foot-rule" style="left:608px;width:190px"></div>
<div class="abs foot-social" style="left:608px;top:2142px"><i></i>Friendspace</div>
<div class="abs foot-social" style="left:608px;top:2184px"><i></i>Chirper</div>
<div class="abs foot-social" style="left:608px;top:2228px"><i></i>Pinboard</div>

<div class="abs foot-title" style="left:824px">NEWS</div>
<div class="abs foot-rule" style="left:824px"></div>
<div class="abs foot-news" style="left:826px;top:2146px" role="img" aria-label="News photo of a youth match"></div>
<p class="abs foot-copy" style="left:902px;top:2146px;width:120px"><b>Lorem ipsum dolor</b><br>sit amet, consectetuer adipiscing elit, sed .</p>
<div class="abs foot-news" style="left:826px;top:2214px" role="img" aria-label="News photo of a field"></div>
<p class="abs foot-copy" style="left:902px;top:2214px;width:120px"><b>Lorem ipsum dolor</b><br>sit amet, consectetuer adipiscing elit, sed .</p>

<div class="abs copyright">Lend a Lantern © 2014 Privacy Policy</div>

</body>
</html>
```